Need help in designing new business card utilizing our new logo.

BuildMarq Solutions works with Construction Business Owners, Managers & IT Professionals to strengthen software usage and increase user productivity.

Our Construction Accounting and Mobile Field Management Software Clients engage with us in the following areas:

New Software Implementations
Software Re-Implementations
Redesigning Software Usage at the User Level
Project Coordination & Management
Continued Software Support

Old tag line:
Weighing Options - Implementing Solutions

www.buildmarq-solutions.example

Stride 4 is a product, but not needed for a new business card.

```html
<!DOCTYPE html>
<html lang="en">
<head>
<meta charset="utf-8">
<title>BuildMarq Solutions – Business Card</title>
<link href="https://fonts.googleapis.com/css2?family=Montserrat:wght@400;500;600;700&family=Arimo:wght@400&display=swap" rel="stylesheet">
<style>
  :root {
    --brand-blue: #2e3192;
    --brand-blue-mid: #5a5ea8;
    --steel-grey: #c4c5cb;
    --soft-grey: #a7a9ac;
    --paper: #ffffff;
    --backdrop: #e9e7e3;
    --ink-light: #ffffff;
  }
  * { box-sizing: border-box; margin: 0; padding: 0; }
  html, body { width: 900px; height: 1200px; overflow: hidden; }
  body {
    background: var(--backdrop);
    position: relative;
    font-family: "Montserrat", Arial, sans-serif;
  }
  .card {
    position: absolute;
    left: 88px;
    width: 732px;
    height: 426px;
    border-radius: 22px;
    overflow: hidden;
  }

  /* Front */
  .card-front {
    top: 126px;
    background: linear-gradient(90deg, var(--brand-blue) 0%, var(--brand-blue) 45%, var(--brand-blue-mid) 68%, var(--steel-grey) 100%);
    color: var(--ink-light);
  }
  .front-brand {
    position: absolute;
    left: 46px;
    top: 36px;
    font-weight: 500;
    line-height: 1;
    color: var(--ink-light);
  }
  .front-brand .brand-line-1 { display: block; font-size: 62px; letter-spacing: 0.01em; }
  .front-brand .brand-line-2 { display: block; font-size: 29px; letter-spacing: 0.42em; margin-top: 10px; }
  .contact {
    position: absolute;
    left: 48px;
    top: 184px;
    font-family: "Arimo", Arial, sans-serif;
  }
  .contact-name { font-family: "Montserrat", Arial, sans-serif; font-weight: 700; font-size: 19px; letter-spacing: 0.02em; }
  .contact-role { font-family: "Montserrat", Arial, sans-serif; font-weight: 600; font-size: 12px; margin-top: 3px; }
  .contact-address { font-size: 16.5px; line-height: 24px; margin-top: 12px; }
  .contact-list { list-style: none; margin-top: 9px; font-size: 16px; }
  .contact-list li { display: flex; align-items: center; height: 23.5px; }
  .contact-list svg { width: 13px; height: 13px; margin-right: 10px; fill: #dcdcec; }
  .front-rule {
    position: absolute;
    left: 48px; right: 52px; top: 374px;
    height: 1px;
    background: rgba(255,255,255,0.85);
  }
  .front-tagline {
    position: absolute;
    left: 48px; right: 52px; top: 389px;
    text-align: center;
    font-size: 14.5px;
    font-weight: 500;
    letter-spacing: 0.03em;
  }

  /* Back */
  .card-back {
    top: 640px;
    background: var(--paper);
  }
  .back-lockup {
    position: absolute;
    left: 138px;
    top: 150px;
    display: flex;
    align-items: center;
  }
  .back-lockup .brand-square {
    width: 92px; height: 92px;
    background: var(--brand-blue);
    margin-right: 40px;
  }
  .back-brand {
    font-weight: 600;
    color: var(--brand-blue);
    line-height: 1;
  }
  .back-brand .brand-line-1 { display: block; font-size: 60px; }
  .back-brand .brand-line-2 { display: block; font-size: 26px; letter-spacing: 0.42em; margin-top: 4px; }
  .back-url {
    position: absolute;
    left: 0; right: 0; top: 352px;
    text-align: center;
    font-size: 17px;
    font-weight: 600;
    letter-spacing: 0.42em;
    color: var(--brand-blue);
    text-transform: uppercase;
  }
  .back-band {
    position: absolute;
    left: 0; right: 0; bottom: 0;
    height: 40px;
  }
  .back-band svg { position: absolute; inset: 0; width: 100%; height: 100%; }
  .back-tagline {
    position: absolute;
    left: 80px; right: 0; top: 0; bottom: 0;
    display: flex; align-items: center; justify-content: center;
    color: var(--ink-light);
    font-size: 20px;
    font-weight: 500;
    text-transform: uppercase;
    letter-spacing: 0.01em;
  }
  .back-tagline strong { font-weight: 700; }
</style>
</head>
<body>

<section class="card card-front" aria-label="Business card front">
  <div class="front-brand">
    <span class="brand-line-1">BUILDMARQ</span>
    <span class="brand-line-2">SOLUTIONS</span>
  </div>

  <div class="contact">
    <p class="contact-name">DANA R. WHITFIELD</p>
    <p class="contact-role">OWNER</p>
    <p class="contact-address">14B Foundry Lane- PMB 118<br>Maple Falls NY 12000</p>
    <ul class="contact-list">
      <li><svg viewBox="0 0 16 16" aria-hidden="true"><path d="M3.6 1.2l2.3 2.7-1.3 1.8c.9 2 2.6 3.8 4.7 4.8l1.8-1.3 2.7 2.3-1.4 2.3C7.3 13.6 2.4 8.7 1.2 3z"/></svg>800-555-0142 ext.100</li>
      <li><svg viewBox="0 0 16 16" aria-hidden="true"><path d="M4 1h8v14H4zM5.3 2.5v9.5h5.4V2.5zM7.2 13h1.6v1H7.2z" fill-rule="evenodd"/></svg>555-014-7731</li>
      <li><svg viewBox="0 0 16 16" aria-hidden="true"><path d="M1 3h14v10H1zM2.2 4.2v.4L8 8.6l5.8-4v-.4zM2.2 6.1v5.7h11.6V6.1L8 10.1z" fill-rule="evenodd"/></svg>dana.whitfield@buildmarq-solutions.example</li>
    </ul>
  </div>

  <div class="front-rule"></div>
  <p class="front-tagline">CONSTRUCTION ACCOUNTING SOFTWARE CONSULTANTS</p>
</section>

<section class="card card-back" aria-label="Business card back">
  <div class="back-lockup">
    <div class="brand-square"></div>
    <div class="back-brand">
      <span class="brand-line-1">BUILDMARQ</span>
      <span class="brand-line-2">SOLUTIONS</span>
    </div>
  </div>

  <p class="back-url">www.buildmarq-solutions.example</p>

  <div class="back-band">
    <svg viewBox="0 0 732 40" preserveAspectRatio="none" aria-hidden="true">
      <polygon points="0,0 54,0 94,40 0,40" fill="var(--steel-grey)"/>
      <polygon points="54,0 732,0 732,40 94,40" fill="var(--brand-blue)"/>
    </svg>
    <p class="back-tagline"><span><strong>Weighing</strong> Options – <strong>Implementing</strong> Solutions</span></p>
  </div>
</section>

</body>
</html>
```